Simon Ashgrove Pianist Teacher Examiner

I need a website design to promote my business as a professional classical pianist and a piano teacher of all levels.
I want it to look a mixture of old world opulence (eg antique grand piano?) and modern text. It should have an elegant, beautiful and relaxing feel.

Industry/Entity Type

Teacher

```html
<!DOCTYPE html>
<html lang="en">
<head>
<meta charset="utf-8">
<title>Simon Ashgrove – Professional Piano Teacher</title>
<link rel="stylesheet" href="https://fonts.googleapis.com/css2?family=Marcellus+SC&family=Source+Sans+3:wght@400;500&display=swap">
<style>
  :root {
    --plum: #92278f;
    --paper: #ffffff;
    --ink: #111111;
    --photo-dark: #2c2c30;
    --photo-mid: #3d3a3a;
    --photo-warm: #8a7658;
  }
  * { margin: 0; padding: 0; box-sizing: border-box; }
  html, body {
    width: 1200px;
    height: 1000px;
    overflow: hidden;
    background: var(--paper);
  }
  .page {
    position: relative;
    width: 1200px;
    height: 1000px;
    font-family: "Source Sans 3", "Myriad Pro", sans-serif;
    color: var(--ink);
  }
  .top-band {
    position: absolute;
    left: 52px; top: 29px;
    width: 1092px; height: 34px;
    background: var(--plum);
  }
  .main-nav {
    position: absolute;
    left: 55px; top: 84px;
    width: 1088px;
  }
  .main-nav ul {
    display: flex;
    justify-content: space-between;
    list-style: none;
  }
  .main-nav a {
    font-family: "Marcellus SC", serif;
    font-size: 29px;
    letter-spacing: 2px;
    color: var(--ink);
    text-decoration: none;
    text-transform: uppercase;
  }
  .main-nav li:last-child { padding-top: 5px; }
  .hero-band {
    position: absolute;
    left: 52px; top: 141px;
    width: 1096px; height: 257px;
    background: var(--plum);
  }
  .hero-tagline {
    position: absolute;
    left: 348px; top: 182px;
    width: 760px;
    font-family: "Marcellus SC", serif;
    font-weight: 400;
    font-size: 46px;
    letter-spacing: 2.5px;
    color: var(--paper);
    white-space: nowrap;
  }
  .hero-name {
    position: absolute;
    left: 664px; top: 258px;
    font-family: "Source Sans 3", sans-serif;
    font-weight: 400;
    font-size: 67px;
    line-height: 1.1;
    color: var(--paper);
    white-space: nowrap;
  }
  .portrait {
    position: absolute;
    left: 84px; top: 254px;
    width: 460px; height: 690px;
    background:
      radial-gradient(ellipse at 55% 40%, var(--photo-mid) 0%, var(--photo-dark) 70%),
      var(--photo-dark);
  }
  .portrait::after {
    content: "";
    position: absolute;
    left: 0; right: 0; bottom: 0;
    height: 30%;
    background: linear-gradient(to bottom, rgba(138,118,88,0), var(--photo-warm));
    opacity: 0.5;
  }
  .intro {
    position: absolute;
    left: 626px; top: 484px;
    width: 518px;
    font-size: 19px;
    line-height: 23.7px;
    text-align: justify;
    text-align-last: justify;
    hyphens: auto;
  }
  .intro-lead { font-size: 24px; }
  .site-footer {
    position: absolute;
    left: 52px; top: 944px;
    width: 1094px; height: 35px;
    background: var(--plum);
    color: var(--paper);
    font-size: 18px;
    line-height: 35px;
    padding-left: 14px;
  }
</style>
</head>
<body>
<div class="page">
  <div class="top-band"></div>

  <nav class="main-nav">
    <ul>
      <li><a href="#">Home</a></li>
      <li><a href="#">Biography</a></li>
      <li><a href="#">Lessons</a></li>
      <li><a href="#">Students</a></li>
      <li><a href="#">Policy</a></li>
      <li><a href="#">Contact</a></li>
    </ul>
  </nav>

  <header class="hero-band"></header>
  <h2 class="hero-tagline">Professional piano teacher</h2>
  <h1 class="hero-name">Simon Ashgrove</h1>

  <div class="portrait" role="img" aria-label="Portrait of the pianist kneeling beside a white piano against a dark studio backdrop"></div>

  <p class="intro"><span class="intro-lead">Lorem ipsum</span> dolor sit amet, consectetur adipsing elit. Curabitur accumsan tristique nibh eget feugiat. Donec tellus massa, euismod quis sem non, aliquam tempus est. In vel nunc in ipsum commodo rutrum vel eu mi. Quisque nec sodales arcu. In feugiat blandit eros ac blandit. Donec porttitor libero feugiat tortor dapibus bibendum. Nunc tincidunt metus non magna condimentum laoreet id sit amet dolor. Nunc est purus, elementum non tortor eget, cursus aliquam</p>

  <footer class="site-footer">©2014 Simon Ashgrove. All right reserved</footer>
</div>
</body>
</html>
```